Ferrobay | Minimalist 6-panel Brochure

Background: Ferro Bay Fabricators Corp. is a manufacturer of steel wire-based products (e.g. nails, galvanized wire, barbed wire, steel matting) in Manila.

Brand Differentiator: Uncompromising "first world" quality to push our "third world" country to develop

Customers: We are a B2B company - we supply the materials to be used by Contractors in building projects. Retailers in selling to home users,Wholesalers in distributing to their retailer networks.

Brochure Objective: Using a standard 6-panel 8.5" x 11" Brochure, to create awareness among contractors and in the architectural community as a leader in quality products and honest service. (architects are big influencers of contractors in that they can recommend quality suppliers to them)

Brochure Contents: I have attached (in Powerpoint) the copy points of the Brochures broken down by 6 panels of content.
**DO NOT MIND how I've layout-ed the info in the .ppt, It's for your easier understanding only**

Brand Essence to Consider: 'First-world' in terms of product standards. Transparent & honest in terms of service/delivery. Approachable from Big to Small customers.

*Bonus Brand Essence: Someone you can have a 'light' conversation with over the phone for a quotation.*

Design Guidelines:
1) Be creative. If you think any of the guidelines I mention below won't be the best fit to your interpretation of my vision, go ahead and do what you think is best!

2) Be minimalist. I've kept the copy points's words at a minimum so there would be more emphasis on the content. Design around the copy points that bring out the gist more and the details less.

3) Design flat. Make the design look simple yet attractive.
PEG: If there was a website that I'd like to take design cues from, it's www.plinthory.com and tovelink.com/purse . Details like font size, font color, etc here were nicely differentiated for Headers, Subtexts and Descriptions. Be playful with using font effects like BOLD and Italics.

4) Use Icons. Instead of using a photo-heavy brochure, it would be better if we created icons for the brochure parts ('Our Thinking', 'How We Serve You', 'How It Works')
PEG: Abstract/minimalist icons such as those seen at the top of quellmarks.com or the middle section of inkvardle.com would be nice.

5) Edit the Product Shots and Pics of our Tech/Machines. Kindly edit and 'beautify' the photos attached to align to your design. Use 1 shot per product. Some are in .jpeg and some in .psd. (see attached. remove the watermarks in .psd shots)

6) Fit the Logo. Feel free to change to color schemes of our logo to make it fit with your designs. (see attached)

7) Front Cover. Kindly go through our 'Tagline' and 'Short Overall Description' first to find inspiration for some simple artwork.
*sidenote: For you to understand our tagline, the Philippines hasn't fully developed a priority for quality in terms of steel materials used in construction. (price had always dictated the market) And we want to help push them to that point in shaping the country's real estate development from 3rd world to a 1st world country's standards.

8) Word Cloud. I've listed 8 of the biggest and well-known projects we've supported in the past 5 years in 'Supported Projects' and my idea is for you to create a nice 'Word Cloud' of it similar to how I presented it in the ppt attached. Or it can be presented in some shape you'd think is nice. (search "word cloud" in Zendro Pictures)

9) Call-to-Action. Make the 'Call-to-Action' panel of the brochure as "inviting" as possible.

10) Be creative. AGAIN. Aside for the copy points in the ppt guidelines attached, I would like to stress that you are free to edit/create whatever you deem fit to my vision. (as you've come to know what I'd like by now)

Don't forget to have fun!! It'll be awesome working with you.

**UPDATE in July 24: Use the PPT v2 for details, attached separately. (now with design pegs)**

**UPDATE in July 29: for the photos under 'First World Tech', please use the Cutter photo and Wire-drawing machine photo attached here.**
Updates

Hello again! Good job so far on the initial designs. To let you know what style I'd like our icons in "How We Serve You", please visit www.ferrobayph.sitevane.com for our mock-up website.

You can also scroll down in the first page in "Our 4 Products" to see how I'd like our fonts to be used here so it'll be readable (i.e. through different font sizes, font effects like Bold & Italic)

As always, if you think you have a better idea on how to execute what I've mentioned above, go do it!

**UPDATE in July 24: Use the PPT v2 for the copy details, attached separately. Now with Design PEGS.**

Reason: extending for a few more days for last-minute submissions/revisions. Thanks!

Target Market(s)

Architectural firms. Building contractors. Steel wholesalers/distributors.

Industry/Entity Type

Real Estate

Requirements
Must have
• Simple. Approachable. Clear. Attractive. Uncluttered.
Should not have
• BULLET POINTS. (this shouldn't look like a Powerpoint material in any way or form)

```html
<!DOCTYPE html>
<html lang="en">
<head>
<meta charset="utf-8">
<title>Ferrobay Manufacturing – Brochure Cover Panels</title>
<link rel="stylesheet" href="https://fonts.googleapis.com/css2?family=Noto+Sans:ital,wght@0,400;1,400&display=swap">
<style>
  :root {
    --steel-blue: #3399cc;
    --charcoal: #4d4d4d;
    --ink: #111111;
    --white: #ffffff;
    --page: #ffffff;
  }
  html, body {
    margin: 0;
    padding: 0;
    width: 1200px;
    height: 1124px;
    overflow: hidden;
    background: var(--page);
  }
  .brochure {
    display: block;
    width: 1200px;
    height: 1124px;
    font-family: "Noto Sans", "DejaVu Sans", Verdana, sans-serif;
  }
  .fill-blue { fill: var(--steel-blue); }
  .fill-charcoal { fill: var(--charcoal); }
  .title { fill: var(--white); }
  .title-initial { font-size: 76px; }
  .title-rest { font-size: 56px; }
  .wordmark { font-size: 58px; font-weight: 400; text-anchor: middle; }
  .wordmark--charcoal { fill: var(--charcoal); }
  .wordmark--blue { fill: var(--steel-blue); }
  .tagline { font-size: 15px; font-style: italic; text-anchor: middle; }
  .tagline--white { fill: var(--white); }
  .tagline--blue { fill: var(--steel-blue); }
  .body-copy { font-size: 19px; fill: var(--white); text-anchor: end; }
  .brand-ink { fill: var(--ink); }
  .brand-blue { fill: var(--steel-blue); }
</style>
</head>
<body>
<svg class="brochure" viewBox="0 0 1068 1000" width="1200" height="1124" role="img" aria-label="Two Ferrobay Manufacturing brochure panels in blue and charcoal">

  <!-- Panel one: blue on charcoal -->
  <g class="panel panel--blue">
    <rect class="fill-charcoal" x="0" y="0" width="470" height="995"/>
    <polygon class="fill-blue" points="30,0 230,0 470,62 470,385 30,268"/>
    <circle class="fill-blue" cx="235" cy="490" r="200"/>
    <polygon class="fill-blue" points="0,578 440,683 440,995 240,995 0,905"/>

    <text class="title" x="50" y="135">
      <tspan class="title-initial">F</tspan><tspan class="title-rest">ERROBAY</tspan>
    </text>
    <text class="title" x="50" y="230" textLength="408" lengthAdjust="spacingAndGlyphs">
      <tspan class="title-initial">M</tspan><tspan class="title-rest">anufacturing</tspan>
    </text>

    <text class="wordmark wordmark--charcoal" x="235" y="510">Ferrobay</text>

    <text class="tagline tagline--white" x="226" y="710">“first-world standards to build the third-world up.”</text>

    <text class="body-copy" x="424" y="780"><tspan class="brand-ink">Ferrobay</tspan> manufactures goods that</text>
    <text class="body-copy" x="424" y="820">are first world in nature &amp; truth-telling in</text>
    <text class="body-copy" x="424" y="860">class. Now you can build Sydney around</text>
    <text class="body-copy" x="424" y="900">Taguig, Shanghai inside Binondo, and</text>
    <text class="body-copy" x="424" y="940">Manhattan across Valero.</text>
  </g>

  <!-- Panel two: charcoal on blue -->
  <g class="panel panel--charcoal">
    <rect class="fill-blue" x="600" y="0" width="468" height="995"/>
    <polygon class="fill-charcoal" points="628,0 825,0 1068,62 1068,385 628,268"/>
    <circle class="fill-charcoal" cx="835" cy="490" r="200"/>
    <polygon class="fill-charcoal" points="600,578 1037,688 1037,995 835,995 600,928"/>

    <text class="title" x="650" y="135">
      <tspan class="title-initial">F</tspan><tspan class="title-rest">ERROBAY</tspan>
    </text>
    <text class="title" x="650" y="230" textLength="408" lengthAdjust="spacingAndGlyphs">
      <tspan class="title-initial">M</tspan><tspan class="title-rest">anufacturing</tspan>
    </text>

    <text class="wordmark wordmark--blue" x="835" y="510">Ferrobay</text>

    <text class="tagline tagline--blue" x="833" y="708">“first-world standards to build the third-world up.”</text>

    <text class="body-copy" x="1025" y="762"><tspan class="brand-blue">Ferrobay</tspan> manufactures goods that</text>
    <text class="body-copy" x="1025" y="802">are first world in nature &amp; truth-telling in</text>
    <text class="body-copy" x="1025" y="842">class. Now you can build Sydney around</text>
    <text class="body-copy" x="1025" y="882">Taguig, Shanghai inside Binondo, and</text>
    <text class="body-copy" x="1025" y="922">Manhattan across Valero.</text>
  </g>
</svg>
</body>
</html>
```